Seed Company Looking For a Soybean Seed Bag Design

We are are a regional seed company who is currently launching a new line of soybean products. The brand of the product will be Tru-Vora. We are looking for a custom design of a soybean bag measuring 16"x5"x30" (when constructed). We are looking for a modern design that's relatively loud, but not too busy. The proof needs to match with the attached template. We have also provided a proof of a previous bag project (Fox-Brook-Standard) we've done to show how the artwork needs to be laid out. In no way does the new design need to resemble the example. Also attached are some other examples of seed bags.
Agriculture
Designer to choose colors to be used in the design.

```html
<!DOCTYPE html>
<html lang="en">
<head>
<meta charset="utf-8">
<title>Tru-Vora Seed Bags</title>
<link href="https://fonts.googleapis.com/css2?family=Bebas+Neue&family=Kaushan+Script&display=swap" rel="stylesheet">
<style>
  :root {
    --page: #ffffff;
    --film: #e9e9e9;
    --seal: #dcdcdc;
    --ink: #151515;
    --corn: #f2bd00;
    --corn-band: #f6d64a;
    --corn-seed-a: #f4a21c;
    --corn-seed-b: #e6c36a;
    --soy: #08722b;
    --soy-band: #3fe27a;
    --soy-seed-a: #d8ac55;
    --soy-seed-b: #b88a3a;
    --tomato: #ff0a0a;
    --tomato-band: #f72a2a;
    --tomato-seed-a: #e8b7a0;
    --tomato-seed-b: #c97b60;
  }
  * { margin: 0; padding: 0; box-sizing: border-box; }
  html, body { width: 1200px; height: 934px; overflow: hidden; background: var(--page); }
  .canvas {
    width: 1200px; height: 934px;
    display: flex; justify-content: center; align-items: center; gap: 22px;
  }
  .bag {
    position: relative;
    width: 336px; height: 740px;
    background: var(--film);
    overflow: hidden;
  }
  .bag__seal {
    height: 42px;
    background: repeating-linear-gradient(90deg, var(--seal) 0 3px, #e4e4e4 3px 6px);
  }
  .bag__brand {
    margin-top: 52px;
    display: flex; align-items: center; justify-content: center; gap: 8px;
    font-family: "Bebas Neue", sans-serif;
    font-size: 34px; line-height: 1; letter-spacing: 1px; color: var(--ink);
  }
  .bag__brand-dot { width: 14px; height: 14px; background: var(--ink); border-radius: 50%; }
  .bag__crop {
    margin-top: 64px;
    padding: 0 18px;
    text-align: center;
    white-space: nowrap;
    font-family: "Bebas Neue", sans-serif;
    font-weight: 400;
    font-size: 100px; line-height: 0.95; letter-spacing: 1px;
    color: var(--ink);
  }
  .bag__seeds {
    margin-top: 8px;
    text-align: center;
    white-space: nowrap;
    font-family: "Kaushan Script", cursive;
    font-size: 76px; line-height: 1.15;
  }
  .bag__band {
    position: absolute; left: 0; right: 0; top: 432px; bottom: 0;
  }
  .bag__art {
    position: absolute; left: 28px; right: 28px; top: 34px; bottom: 40px;
    border-radius: 48% 48% 40% 40% / 30% 30% 24% 24%;
  }
  .bag--corn .bag__seeds { color: var(--corn); }
  .bag--corn .bag__band { background: var(--corn-band); }
  .bag--corn .bag__art { background: radial-gradient(circle at 45% 45%, var(--corn-seed-a), var(--corn-seed-b)); }
  .bag--soy .bag__seeds { color: var(--soy); }
  .bag--soy .bag__band { background: var(--soy-band); }
  .bag--soy .bag__art { background: radial-gradient(circle at 45% 45%, var(--soy-seed-a), var(--soy-seed-b)); }
  .bag--tomato .bag__seeds { color: var(--tomato); }
  .bag--tomato .bag__band { background: var(--tomato-band); }
  .bag--tomato .bag__art { background: radial-gradient(circle at 45% 45%, var(--tomato-seed-a), var(--tomato-seed-b)); }
</style>
</head>
<body>
<main class="canvas">
  <section class="bag bag--corn">
    <div class="bag__seal"></div>
    <div class="bag__brand"><span class="bag__brand-dot"></span>Tru-Vora</div>
    <h2 class="bag__crop">CORN</h2>
    <p class="bag__seeds">seeds</p>
    <div class="bag__band">
      <div class="bag__art" role="img" aria-label="Corn cob silhouettes filled with a photo of corn kernels"></div>
    </div>
  </section>
  <section class="bag bag--soy">
    <div class="bag__seal"></div>
    <div class="bag__brand"><span class="bag__brand-dot"></span>Tru-Vora</div>
    <h2 class="bag__crop">SOYBEAN</h2>
    <p class="bag__seeds">seeds</p>
    <div class="bag__band">
      <div class="bag__art" role="img" aria-label="Two soybean silhouettes filled with a photo of soybeans"></div>
    </div>
  </section>
  <section class="bag bag--tomato">
    <div class="bag__seal"></div>
    <div class="bag__brand"><span class="bag__brand-dot"></span>Tru-Vora</div>
    <h2 class="bag__crop">TOMATO</h2>
    <p class="bag__seeds">seeds</p>
    <div class="bag__band">
      <div class="bag__art" role="img" aria-label="Two tomato silhouettes filled with a photo of tomato seeds"></div>
    </div>
  </section>
</main>
</body>
</html>
```